Edits to Existing Flyer

Re create this file for us with new look and feel and updated information.
Updates

Hi, We do not want/need any more submissions. The field is down to two designers. Thank you all for your time.

Target Market(s)

homeless veterans, veterans, veteran families

Font styles to use
Serif

Colors
abd036
9bcb3c
33a6d7
0255a3
3176b5

Requirements
Must have
• approved photos, readable text

```html
<!DOCTYPE html>
<html lang="en">
<head>
<meta charset="utf-8">
<title>Harborlight Veterans – Supportive Services Brochure</title>
<link href="https://fonts.googleapis.com/css2?family=Cinzel:wght@600&family=Open+Sans:wght@400;700;800&family=Oswald:wght@600;700&display=swap" rel="stylesheet">
<style>
  :root{
    --green:#9bcb3c;
    --green-light:#abd036;
    --sky:#33a6d7;
    --navy:#0255a3;
    --blue:#3176b5;
    --ink:#1d1d1f;
    --dark:#2a2a2c;
    --paper:#ffffff;
    --bg:#e4e4e4;
    --grey-text:#4a4a4a;
  }
  *{box-sizing:border-box;margin:0;padding:0}
  html,body{width:1200px;height:803px;overflow:hidden;background:var(--bg)}
  body{position:relative;font-family:"Open Sans",sans-serif}

  .page{position:absolute;top:52px;width:530px;height:700px;overflow:hidden;background:var(--paper)}
  .page--back{left:70px}
  .page--cover{left:600px}

  /* back page */
  .brand{position:absolute;left:64px;top:92px;display:flex;align-items:center;gap:10px}
  .brand__mark{width:26px;height:26px;border-radius:50%;background:var(--blue)}
  .brand__name{font-family:"Cinzel",serif;font-weight:600;font-size:24px;color:var(--blue);letter-spacing:.5px}
  .project-title{position:absolute;left:64px;top:140px;font-weight:800;font-size:15px;color:var(--ink);letter-spacing:.3px}
  .contact{position:absolute;left:64px;top:172px;list-style:none}
  .contact li{display:flex;align-items:center;gap:12px;font-size:13px;color:var(--grey-text);height:25px}
  .contact svg{width:16px;height:16px;flex:none}
  .funding{position:absolute;left:64px;top:258px;color:var(--grey-text)}
  .funding__lead{font-size:11px;text-transform:uppercase;letter-spacing:.3px}
  .funding__title{font-weight:800;font-size:27px;color:var(--blue);line-height:1.1}
  .funding__source{font-size:11px;text-transform:uppercase;letter-spacing:.3px}
  .area-map{position:absolute;left:190px;top:330px;width:340px;height:270px;
    background:linear-gradient(135deg,#efefec 0%,#e0e0dc 55%,#d6d6d2 100%)}
  .partner-bands{position:absolute;left:0;top:400px;width:530px;height:220px}
  .partner{position:absolute;font-weight:700;font-size:11px;line-height:1.15;display:flex;align-items:center;gap:8px}
  .partner--renewal{left:40px;top:470px;color:var(--navy)}
  .partner--alliance{left:40px;top:540px;color:var(--navy)}
  .partner__badge{width:26px;height:26px;border-radius:50%;background:var(--navy);flex:none}
  .hotline{position:absolute;left:0;bottom:0;width:530px;height:92px;background:var(--blue);
    display:flex;align-items:center;justify-content:center;color:#fff;font-size:24px;letter-spacing:.5px}

  /* cover */
  .cover-photo{position:absolute;inset:0;
    background:linear-gradient(160deg,#d9dcdc 0%,#b9b6ae 35%,#8f8a7c 60%,#6d6a5e 100%)}
  .cover-band{position:absolute;left:0;top:0;width:530px;height:700px}
  .ribbon{position:absolute;left:0;top:360px;height:34px;padding:0 26px 0 14px;background:var(--ink);
    display:flex;align-items:center;font-family:"Cinzel",serif;font-weight:600;font-size:19px;color:#fff}
  .cover-brand{position:absolute;left:26px;top:560px;font-family:"Cinzel",serif;font-weight:600;font-size:12px;color:#fff;display:flex;align-items:center;gap:6px}
  .cover-brand__mark{width:12px;height:12px;background:#fff;border-radius:50%}
  .headline{position:absolute;left:190px;top:430px;font-family:"Oswald",sans-serif;font-weight:700;line-height:.95;text-transform:uppercase}
  .headline__lead{display:block;color:var(--green-light);font-size:30px;margin-left:44px}
  .headline__row{display:flex;align-items:flex-start}
  .headline__for{color:#fff;font-size:30px;writing-mode:vertical-rl;transform:rotate(180deg);margin-right:6px;line-height:1}
  .headline__main{color:var(--sky);font-size:66px;line-height:.92}
</style>
</head>
<body>

<section class="page page--back">
  <div class="brand">
    <span class="brand__mark"></span>
    <span class="brand__name">Harborlight Veterans</span>
  </div>
  <p class="project-title">BAYSIDE COMMUNITY RENEWAL PROJECT</p>

  <ul class="contact">
    <li>
      <svg viewBox="0 0 16 16"><rect width="16" height="16" rx="3" fill="var(--blue)"/><path d="M5 3.5l2 2-1 1.3c.6 1.3 1.6 2.3 2.9 2.9l1.3-1 2 2-1.2 1.5C8 12 4 8 3.8 4.7z" fill="#fff"/></svg>
      555.014.7100
    </li>
    <li>
      <svg viewBox="0 0 16 16"><rect width="16" height="16" rx="3" fill="var(--blue)"/><circle cx="8" cy="8" r="4.5" fill="none" stroke="#fff" stroke-width="1.2"/><path d="M3.5 8h9M8 3.5c-2 2.5-2 6.5 0 9M8 3.5c2 2.5 2 6.5 0 9" fill="none" stroke="#fff" stroke-width="1"/></svg>
      harborlightvets.example
    </li>
    <li>
      <svg viewBox="0 0 16 16"><rect width="16" height="16" rx="3" fill="var(--blue)"/><path d="M8 3a3.2 3.2 0 0 0-3.2 3.2C4.8 9 8 13 8 13s3.2-4 3.2-6.8A3.2 3.2 0 0 0 8 3z" fill="#fff"/><circle cx="8" cy="6.2" r="1.2" fill="var(--blue)"/></svg>
      1840 CEDAR ROW, FAIRHAVEN, CA 90000
    </li>
  </ul>

  <div class="funding">
    <p class="funding__lead">Funding for the supportive services for</p>
    <p class="funding__title">VETERAN FAMILIES(SSVF)</p>
    <p class="funding__source">Provided by the Federal Veterans Office</p>
  </div>

  <div class="area-map" role="img" aria-label="Street map showing the office location"></div>

  <svg class="partner-bands" viewBox="0 0 530 220" aria-hidden="true">
    <polygon points="0,0 150,0 280,50 0,50" fill="var(--dark)"/>
    <polygon points="0,50 280,50 330,80 250,110 0,110" fill="#8fd0ee"/>
    <polygon points="0,110 250,110 0,110" fill="var(--dark)"/>
    <polygon points="0,118 320,118 360,150 330,185 0,185" fill="var(--green)"/>
    <polygon points="0,185 330,185 340,220 0,220" fill="var(--dark)"/>
  </svg>
  <div class="partner partner--renewal"><span class="partner__badge"></span>BAYSIDE COMMUNITY<br>RENEWAL PROJECT</div>
  <div class="partner partner--alliance"><span class="partner__badge"></span>Good Neighbor Alliance<br>BAY COUNTY</div>

  <div class="hotline">HOTLINE : 555-013-1200</div>
</section>

<section class="page page--cover">
  <div class="cover-photo" role="img" aria-label="Photo of a smiling soldier in uniform holding his young son"></div>
  <svg class="cover-band" viewBox="0 0 530 700" aria-hidden="true">
    <polygon points="0,420 530,300 530,560 230,700 0,700" fill="var(--dark)" opacity=".94"/>
  </svg>
  <div class="ribbon">Harborlight Veterans</div>
  <div class="cover-brand"><span class="cover-brand__mark"></span>Harborlight Veterans</div>
  <h1 class="headline">
    <span class="headline__lead">Supportive Services</span>
    <span class="headline__row">
      <span class="headline__for">for</span>
      <span class="headline__main">Veteran<br>Families</span>
    </span>
  </h1>
</section>

</body>
</html>
```